Marbleton Health group for a medical office

We need a website created that for our new medical office that will support online booking for appointments. You designed the logo already.

```html
<!DOCTYPE html>
<html lang="en">
<head>
<meta charset="utf-8">
<title>Marbleton Health Group</title>
<link href="https://fonts.googleapis.com/css2?family=Poppins:wght@300;400;500;600;700&display=swap" rel="stylesheet">
<style>
:root{
  --navy:#0b1f44;
  --navy-deep:#071633;
  --blue:#1d4b91;
  --blue-light:#2f62ad;
  --ink:#1b1f2a;
  --muted:#3d4350;
  --pale:#eef1f5;
  --white:#ffffff;
  --check:#43b05c;
  --black:#050505;
}
*{margin:0;padding:0;box-sizing:border-box}
html,body{width:1200px;height:5021px;overflow:hidden}
body{font-family:'Poppins',sans-serif;color:var(--ink);background:var(--white);position:relative}
.abs{position:absolute}
.section{position:absolute;left:0;width:1200px}
.btn{position:absolute;display:flex;align-items:center;justify-content:center;gap:8px;font-size:12.5px;font-weight:500;border-radius:2px;height:42px}
.btn svg{width:11px;height:11px}
.btn-blue{background:var(--blue);color:var(--white)}
.btn-outline{border:2px solid var(--white);color:var(--white)}
.btn-white{background:var(--white);color:var(--navy)}
.title{font-size:35px;font-weight:300;letter-spacing:.5px;text-transform:uppercase}
.title b{font-weight:700}
.photo{position:absolute}

/* hero */
.hero{top:0;height:805px;background:radial-gradient(ellipse at 70% 40%,#163567 0%,var(--navy) 55%,var(--navy-deep) 100%);color:var(--white)}
.brand{position:absolute;left:113px;top:38px;display:flex;align-items:center;gap:10px;color:var(--white);font-weight:600;line-height:1}
.brand .dot{width:56px;height:56px;border:3px solid var(--white);border-radius:50%}
.brand .name{font-size:27px;letter-spacing:.5px}
.brand .sub{font-size:11px;letter-spacing:5px;margin-top:4px}
.nav{position:absolute;left:464px;top:58px;display:flex;gap:22px;font-size:12.5px;font-weight:500}
.nav .active{color:#6ea0ea}
.hero h1{position:absolute;left:115px;top:236px;font-size:39px;line-height:52px;font-weight:300}
.hero h1 b{font-weight:700}
.hero p{position:absolute;left:117px;top:414px;width:500px;font-size:14.5px;line-height:30px}
.hero .rule{position:absolute;left:90px;top:680px;width:1018px;height:1px;background:rgba(255,255,255,.25)}
.feature{position:absolute;top:730px;display:flex;align-items:center;gap:10px;font-size:14.5px;font-weight:500}
.tick{width:15px;height:15px}

/* about */
.about{top:805px;height:549px;background:linear-gradient(120deg,#f4f6f9,#ffffff 60%,#eef1f6)}
.ring{position:absolute;border-radius:50%}
.body-text{position:absolute;font-size:13px;line-height:22.5px;color:var(--muted)}

/* services */
.services{top:1354px;height:789px;background:var(--white)}
.card-label{position:absolute;width:282px;text-align:center;font-size:14px;font-weight:500;line-height:23px;text-transform:uppercase;color:var(--ink)}

/* booking */
.booking{top:2143px;height:380px;background:radial-gradient(ellipse at 50% 50%,#16376c,var(--navy) 70%);color:var(--white);text-align:center}

/* why */
.why{top:2523px;height:594px;background:var(--white)}
.list{position:absolute;left:138px;top:2802px;list-style:none;font-size:12.8px;color:var(--muted)}
.list li{display:flex;align-items:center;gap:9px;height:37px}
.list svg{width:13px;height:13px}

/* care */
.care{top:3117px;height:520px;background:linear-gradient(90deg,#e3e7ed,#f3f4f6)}

/* testimonial */
.testi{top:3637px;height:590px;background:linear-gradient(180deg,#f6f7fa,#eef1f6)}
.card{position:absolute;left:288px;top:3838px;width:624px;height:292px;background:var(--white);box-shadow:0 6px 24px rgba(20,40,80,.12)}
.arrow{position:absolute;font-size:24px;color:var(--ink);font-weight:600}

/* cta */
.cta{top:4227px;height:370px;background:radial-gradient(ellipse at 50% 50%,#16376c,var(--navy) 70%);color:var(--white);text-align:center}

/* footer */
.footer{top:4597px;height:424px;background:var(--black);color:var(--white)}
.foot-links{position:absolute;top:4758px;left:0;width:1200px;display:flex;justify-content:center;gap:22px;font-size:12.5px}
.contact{position:absolute;top:4816px;display:flex;align-items:center;gap:14px;font-size:13.5px;line-height:24px}
.icon-circle{width:40px;height:40px;border-radius:50%;background:var(--blue);display:flex;align-items:center;justify-content:center}
.icon-circle svg{width:16px;height:16px}
.center{position:absolute;left:0;width:1200px;text-align:center}
</style>
</head>
<body>

<!-- HERO -->
<section class="section hero">
  <div class="brand"><span class="dot"></span><div><div class="name">MARBLETON</div><div class="sub">HEALTH GROUP</div></div></div>
  <nav class="nav"><span class="active">Home</span><span>About Us</span><span>What We Offer ▾</span><span>Patients</span><span>Resources</span></nav>
  <div class="btn btn-blue" style="left:902px;top:49px;width:172px;height:41px">Book an Appointment</div>
  <h1>ON-TIME CARE.<br><b>MODERN MEDICINE.</b><br>TRUSTED HEALTH PARTNERS.</h1>
  <p>Marbleton Health Group delivers high-quality medical care with compassion, precision, and efficient scheduling.</p>
  <div class="btn btn-blue" style="left:115px;top:512px;width:146px">Get in Touch <svg viewBox="0 0 12 12"><circle cx="6" cy="6" r="6" fill="#fff"/><path d="M5 3.5 7.5 6 5 8.5" stroke="#1d4b91" stroke-width="1.6" fill="none"/></svg></div>
  <div class="btn btn-outline" style="left:271px;top:512px;width:144px">Learn More <svg viewBox="0 0 12 12"><circle cx="6" cy="6" r="6" fill="#fff"/><path d="M5 3.5 7.5 6 5 8.5" stroke="#0b1f44" stroke-width="1.6" fill="none"/></svg></div>
  <div class="photo" role="img" aria-label="Smiling doctor in a white coat with arms crossed" style="left:718px;top:170px;width:370px;height:460px;border-radius:50% 50% 48% 48%;background:radial-gradient(circle at 50% 35%,#f4f4f4,#c9cfd8 70%,#9aa6b8)"></div>
  <div class="rule"></div>
  <div class="feature" style="left:162px"><svg class="tick" viewBox="0 0 16 16"><circle cx="8" cy="8" r="8" fill="var(--check)"/><path d="M4.5 8.2 7 10.6 11.5 5.8" stroke="#fff" stroke-width="1.8" fill="none"/></svg>Same-day &amp; scheduled appointments</div>
  <div class="feature" style="left:532px"><svg class="tick" viewBox="0 0 16 16"><circle cx="8" cy="8" r="8" fill="var(--check)"/><path d="M4.5 8.2 7 10.6 11.5 5.8" stroke="#fff" stroke-width="1.8" fill="none"/></svg>Patient-first medical care</div>
  <div class="feature" style="left:810px"><svg class="tick" viewBox="0 0 16 16"><circle cx="8" cy="8" r="8" fill="var(--check)"/><path d="M4.5 8.2 7 10.6 11.5 5.8" stroke="#fff" stroke-width="1.8" fill="none"/></svg>Secure online booking</div>
</section>

<!-- ABOUT -->
<section class="section about">
  <div class="ring" style="left:118px;top:125px;width:446px;height:446px;border:7px solid var(--navy);border-right-color:transparent;border-bottom-color:transparent;transform:rotate(-20deg)"></div>
  <div class="photo" role="img" aria-label="Modern glass medical office building" style="left:130px;top:131px;width:440px;height:440px;border-radius:50%;background:linear-gradient(180deg,#8fb6e4 0%,#3f6da8 55%,#6b8a5d 85%,#4a4f55 100%)"></div>
</section>
<div class="title abs" style="left:647px;top:937px;color:var(--blue)">About <b style="color:var(--ink)">Health Group</b></div>
<div class="body-text" style="left:647px;top:1002px;width:424px">Lorem ipsum dolor sit amet, consectetur adipiscing elit, sed do eiusmod tempor incididunt ut labore et dolore magna aliqua. Ut enim ad minim veniam, quis nostrud exercitation ullamco laboris nisi ut aliquip ex ea commodo consequat. Duis aute irure dolor in reprehenderit in voluptate velit esse cillum dolore eu fugiat nulla pariatur. Excepteur sint occaecat cupidatat non proident, sunt in culpa qui officia deserunt mollit anim id est laborum</div>
<div class="body-text" style="left:647px;top:1181px;width:424px">Lorem ipsum dolor sit amet, consectetur adipiscing elit, sed do eiusmod tempor incididunt ut labore et dolore magna aliqua. Ut enim ad minim veniam, quis nostrud.</div>
<div class="btn btn-blue" style="left:647px;top:1280px;width:146px">Learn More <svg viewBox="0 0 12 12"><circle cx="6" cy="6" r="6" fill="#fff"/><path d="M5 3.5 7.5 6 5 8.5" stroke="#1d4b91" stroke-width="1.6" fill="none"/></svg></div>

<!-- SERVICES -->
<section class="section services"></section>
<div class="title center" style="top:1485px;color:var(--blue)">Comprehensive <b style="color:var(--ink)">Medical Care</b></div>
<div class="center" style="top:1550px;font-size:13px;line-height:23px;color:var(--muted)">Our clinic offers a full range of outpatient medical services designed to support your<br>long-term health and wellness.</div>
<div class="photo" role="img" aria-label="Patient giving a high five to her physiotherapist" style="left:8px;top:1627px;width:282px;height:315px;background:linear-gradient(160deg,#dfe4ea,#9fb3c6 60%,#6d8197)"></div>
<div class="photo" role="img" aria-label="Hand pouring blue capsules from a pill bottle" style="left:308px;top:1627px;width:282px;height:315px;background:linear-gradient(160deg,#f1efec,#d9c2ad 60%,#b68a69)"></div>
<div class="photo" role="img" aria-label="Nurse helping an elderly patient walk" style="left:608px;top:1627px;width:282px;height:315px;background:linear-gradient(160deg,#d8d4cf,#8c9bb3 60%,#3f4f6c)"></div>
<div class="photo" role="img" aria-label="Doctor reviewing a tablet with a patient" style="left:906px;top:1627px;width:282px;height:315px;background:linear-gradient(160deg,#eef0f2,#c7d0da 60%,#7f8fa3)"></div>
<div class="card-label" style="left:8px;top:1968px">Primary &amp; Preventive<br>Care</div>
<div class="card-label" style="left:308px;top:1968px">Chronic Condition<br>Management</div>
<div class="card-label" style="left:608px;top:1968px">Acute &amp; Same-Day<br>Visits</div>
<div class="card-label" style="left:906px;top:1968px">Follow-Up &amp;<br>Ongoing Care</div>

<!-- BOOKING -->
<section class="section booking">
  <div class="title" style="position:absolute;top:88px;width:1200px;color:var(--white)">Book Your Appointment <b>In Minutes</b></div>
  <div style="position:absolute;top:155px;width:1200px;font-size:13px;line-height:24px">Our secure, easy-to-use online scheduling system allows you to book appointments anytime, from anywhere. Choose your<br>preferred appointment type and time, receive instant confirmation, and manage your visits with confidence.</div>
  <div class="btn btn-blue" style="left:493px;top:236px;width:214px;height:41px">Schedule Online Now <svg viewBox="0 0 12 12"><circle cx="6" cy="6" r="6" fill="#fff"/><path d="M5 3.5 7.5 6 5 8.5" stroke="#1d4b91" stroke-width="1.6" fill="none"/></svg></div>
</section>

<!-- WHY -->
<section class="section why">
  <div class="ring" style="left:640px;top:81px;width:446px;height:446px;border:7px solid var(--navy);border-right-color:transparent;border-bottom-color:transparent;transform:rotate(-20deg)"></div>
  <div class="photo" role="img" aria-label="Caring hands held together in support" style="left:652px;top:87px;width:440px;height:440px;border-radius:50%;background:linear-gradient(150deg,#d9d9d9,#b08a73 55%,#6d4f3f)"></div>
</section>
<div class="title abs" style="left:138px;top:2648px;color:var(--blue)">Why <b style="color:var(--ink)">Choose Us</b></div>
<div class="body-text" style="left:138px;top:2713px;width:420px;font-size:12.8px">Lorem ipsum dolor sit amet, consectetur adipiscing elit, sed do eiusmod tempor incididunt ut labore et dolore magna aliqua. Ut enim ad minim veniam, quis nostrud.</div>
<ul class="list">
  <li><svg viewBox="0 0 14 14"><circle cx="7" cy="7" r="7" fill="var(--blue)"/><path d="M4 7.2 6.2 9.2 10 5" stroke="#fff" stroke-width="1.6" fill="none"/></svg>Experienced and compassionate medical professionals</li>
  <li><svg viewBox="0 0 14 14"><circle cx="7" cy="7" r="7" fill="var(--blue)"/><path d="M4 7.2 6.2 9.2 10 5" stroke="#fff" stroke-width="1.6" fill="none"/></svg>Modern facility with advanced clinical standards</li>
  <li><svg viewBox="0 0 14 14"><circle cx="7" cy="7" r="7" fill="var(--blue)"/><path d="M4 7.2 6.2 9.2 10 5" stroke="#fff" stroke-width="1.6" fill="none"/></svg>On-time appointments and efficient workflows</li>
  <li><svg viewBox="0 0 14 14"><circle cx="7" cy="7" r="7" fill="var(--blue)"/><path d="M4 7.2 6.2 9.2 10 5" stroke="#fff" stroke-width="1.6" fill="none"/></svg>Secure digital systems and patient privacy focus</li>
  <li><svg viewBox="0 0 14 14"><circle cx="7" cy="7" r="7" fill="var(--blue)"/><path d="M4 7.2 6.2 9.2 10 5" stroke="#fff" stroke-width="1.6" fill="none"/></svg>Clear communication and personalized care plans</li>
</ul>

<!-- CARE -->
<section class="section care">
  <div class="photo" role="img" aria-label="Physiotherapist guiding an older patient through an arm stretch" style="left:0;top:0;width:653px;height:520px;background:linear-gradient(120deg,#c9d2dc,#5b7391 50%,#2c3f58)"></div>
</section>
<div class="title abs" style="left:651px;top:3222px;color:var(--blue)">Care That Respects</div>
<div class="title abs" style="left:651px;top:3266px"><b>Your Time</b></div>
<div class="body-text" style="left:651px;top:3332px;width:430px;font-size:12.8px">We understand that healthcare should feel calm, clear, and supportive. Our team is committed to creating an environment where patients feel informed, respected, and confident in every medical decision.</div>
<div class="body-text" style="left:651px;top:3445px;width:460px;font-size:12.8px">From check-in to follow-up, your experience is designed with care.</div>
<div class="abs" style="left:657px;top:3505px;width:50px;height:50px;border-radius:50%;background:var(--blue);display:flex;align-items:center;justify-content:center"><svg width="18" height="18" viewBox="0 0 24 24"><path d="M6.6 10.8a15 15 0 0 0 6.6 6.6l2.2-2.2a1 1 0 0 1 1-.25 11.4 11.4 0 0 0 3.6.57 1 1 0 0 1 1 1V20a1 1 0 0 1-1 1A17 17 0 0 1 3 4a1 1 0 0 1 1-1h3.5a1 1 0 0 1 1 1c0 1.25.2 2.45.57 3.57a1 1 0 0 1-.25 1z" fill="#fff"/></svg></div>
<div class="abs" style="left:720px;top:3501px;font-size:12px;color:var(--blue-light)">Connect With Us</div>
<div class="abs" style="left:720px;top:3523px;font-size:16px;font-weight:600">+1 (888) 888 8888</div>

<!-- TESTIMONIAL -->
<section class="section testi"></section>
<div class="title center" style="top:3741px;color:var(--blue)">Patients <b style="color:var(--ink)">Testimonial</b></div>
<div class="card"></div>
<div class="photo" role="img" aria-label="Portrait of a smiling patient in a white shirt" style="left:302px;top:3847px;width:261px;height:269px;background:linear-gradient(180deg,#e4e4e4,#c5c2bf 60%,#eeeeee)"></div>
<div class="abs" style="left:338px;top:4122px;width:230px;height:8px;background:#c9ccd2"></div>
<div class="abs" style="left:596px;top:3891px;font-size:15px;font-weight:600">JENNA MARLOW</div>
<div class="abs" style="left:596px;top:3922px;font-size:12.5px;color:var(--blue-light)">3 Days Ago</div>
<div class="body-text" style="left:598px;top:3955px;width:278px;font-size:12.8px">Lorem ipsum dolor sit amet, consectetur adipiscing elit, sed do eiusmod tempor incididunt ut labore et dolore magna aliqua. Ut enim ad minim veniam, quis nostrud.</div>
<div class="arrow" style="left:232px;top:3950px">«</div>
<div class="arrow" style="left:946px;top:3950px">»</div>

<!-- CTA -->
<section class="section cta">
  <div class="title" style="position:absolute;top:103px;width:1200px;color:var(--white)">Take Control of <b>Your Health Today</b></div>
  <div style="position:absolute;top:167px;width:1200px;font-size:12.8px">Whether you are scheduling a routine visit or seeking ongoing care, Marbleton Health Group is here to support you.</div>
  <div style="position:absolute;top:202px;width:1200px;font-size:12.8px">BOOK YOUR APPOINTMENT ONLINE OR CONTACT OUR TEAM TODAY.</div>
  <div class="btn btn-blue" style="left:436px;top:250px;width:215px;height:41px">Book an Appointment <svg viewBox="0 0 12 12"><circle cx="6" cy="6" r="6" fill="#fff"/><path d="M5 3.5 7.5 6 5 8.5" stroke="#1d4b91" stroke-width="1.6" fill="none"/></svg></div>
  <div class="btn btn-white" style="left:662px;top:250px;width:113px;height:41px">Call Us <svg viewBox="0 0 12 12"><circle cx="6" cy="6" r="6" fill="#0b1f44"/><path d="M5 3.5 7.5 6 5 8.5" stroke="#fff" stroke-width="1.6" fill="none"/></svg></div>
</section>

<!-- FOOTER -->
<footer class="section footer">
  <div class="brand" style="left:474px;top:75px"><span class="dot"></span><div><div class="name">MARBLETON</div><div class="sub">HEALTH GROUP</div></div></div>
</footer>
<div class="foot-links"><span>Home</span><span>About Us</span><span>What We Offer ▾</span><span>Patients</span><span>Resources</span><span>Contact us</span></div>
<div class="contact" style="left:194px;color:var(--white)"><span class="icon-circle"><svg viewBox="0 0 24 24"><path d="M12 2a7 7 0 0 0-7 7c0 5.2 7 13 7 13s7-7.8 7-13a7 7 0 0 0-7-7zm0 9.5A2.5 2.5 0 1 1 12 6.5a2.5 2.5 0 0 1 0 5z" fill="#fff"/></svg></span><span>123, Lorum Ipsum Dolor,<br>Sit amet,USA</span></div>
<div class="contact" style="left:506px;color:var(--white)"><span class="icon-circle"><svg viewBox="0 0 24 24"><path d="M3 5h18v14H3z" fill="#fff"/><path d="M3 5l9 7 9-7" stroke="#1d4b91" stroke-width="1.8" fill="none"/></svg></span><span>info@companyname.com</span></div>
<div class="contact" style="left:853px;color:var(--white)"><span class="icon-circle"><svg viewBox="0 0 24 24"><path d="M6.6 10.8a15 15 0 0 0 6.6 6.6l2.2-2.2a1 1 0 0 1 1-.25 11.4 11.4 0 0 0 3.6.57 1 1 0 0 1 1 1V20a1 1 0 0 1-1 1A17 17 0 0 1 3 4a1 1 0 0 1 1-1h3.5a1 1 0 0 1 1 1c0 1.25.2 2.45.57 3.57a1 1 0 0 1-.25 1z" fill="#fff"/></svg></span><span>+1 (888) 888 8888</span></div>
<div class="center" style="top:4904px;font-size:12px;color:var(--white)">© Marbleton Health Group. All Rights Reserved.</div>
<div class="center" style="top:4929px;font-size:12px;color:var(--white)">Privacy Policy | Terms &amp; Conditions</div>

</body>
</html>
```